Modern Innovative Business Card Design

We require a nice, modern, clean business card design, ready for upload to Cardomora. Our company develops online banking software solutions for small financial insitutions. The design should be clean, professional, but yet not "corporate boring". See www.fyrolt.com for an idea of business image and profile. The design should communicate innovation, be modern and fresh, yet look professional and established.

Target Market(s)

Finance industry, bankers, entrepreneurs

Industry/Entity Type

Financial

Contact Information for Business Card

Tobias Wendlerup
CEO

FYROLT BV
Lindenwerf 38
1027 HX Amsterdam
The Netherlands

Phone: +31 20 517 8036
Direct: +31 20 604 1758
Skype: tobias.fyrolt
ceo@fyrolt.com
www.fyrolt.com

Font styles to use
Sans Serif

Requirements
Must have
• Should look clean, modern and professional. File should be ready for upload to cardomora.
Should not have
• Boring standard corporate layout

```html
<!DOCTYPE html>
<html lang="en">
<head>
<meta charset="utf-8">
<title>FYROLT Business Card</title>
<link rel="stylesheet" href="https://fonts.googleapis.com/css2?family=Open+Sans:wght@400;600;700&display=swap">
<style>
  :root {
    --green: #8cc01f;
    --green-dark: #6f9e12;
    --charcoal: #4a4a4d;
    --text-grey: #5a5a5d;
    --card: #ffffff;
    --backdrop: #e7e8ea;
  }
  * { margin: 0; padding: 0; box-sizing: border-box; }
  html, body { width: 1200px; height: 900px; overflow: hidden; }
  body {
    background: var(--backdrop);
    font-family: "Open Sans", Arial, sans-serif;
    position: relative;
  }
  .card {
    position: absolute;
    left: 250px;
    width: 700px;
    height: 400px;
    background: var(--card);
    border-radius: 26px;
    overflow: hidden;
    box-shadow: 0 6px 22px rgba(0,0,0,0.14);
  }
  .card-back { top: 40px; }
  .card-front { top: 465px; }
  .card-shapes { position: absolute; inset: 0; width: 100%; height: 100%; }

  .wordmark {
    position: absolute;
    display: flex;
    align-items: center;
    gap: 10px;
    color: var(--charcoal);
    font-weight: 600;
    letter-spacing: 0.08em;
  }
  .wordmark-square { width: 14px; height: 14px; background: var(--green); }
  .card-back .wordmark { left: 48px; top: 290px; font-size: 50px; }
  .card-back .wordmark-square { width: 18px; height: 18px; }
  .card-front .wordmark { left: 48px; top: 70px; font-size: 44px; }

  .holder { position: absolute; right: 46px; top: 40px; }
  .holder-name { color: var(--green); font-weight: 700; font-size: 17px; }
  .holder-role { color: var(--text-grey); font-size: 15px; }

  .contact {
    position: absolute;
    left: 410px; top: 150px;
    display: grid;
    grid-template-columns: auto auto;
    column-gap: 10px;
    row-gap: 1px;
    font-size: 16px;
    line-height: 21px;
  }
  .contact dt { color: var(--green); text-align: right; }
  .contact dd { color: var(--text-grey); }

  .address {
    position: absolute;
    left: 48px; top: 216px;
    font-style: normal;
    color: var(--text-grey);
    font-size: 17px;
    line-height: 24px;
  }
  .address .web { color: var(--green); font-weight: 600; }
</style>
</head>
<body>

<section class="card card-back" aria-label="Card back">
  <svg class="card-shapes" viewBox="0 0 700 400" aria-hidden="true">
    <polygon points="430,0 700,0 700,175 585,110" fill="var(--charcoal)"/>
    <polygon points="300,240 430,150 700,120 700,200" fill="var(--green)"/>
    <polygon points="255,400 480,280 700,255 700,400" fill="var(--charcoal)"/>
  </svg>
  <div class="wordmark"><span class="wordmark-square"></span>FYROLT</div>
</section>

<section class="card card-front" aria-label="Card front">
  <svg class="card-shapes" viewBox="0 0 700 400" aria-hidden="true">
    <path d="M0,318 C180,312 340,292 480,258 C350,300 180,330 0,348 Z" fill="var(--charcoal)"/>
    <path d="M0,362 C260,352 500,305 700,255 L700,400 L0,400 Z" fill="var(--green)"/>
  </svg>

  <div class="wordmark"><span class="wordmark-square"></span>FYROLT</div>

  <div class="holder">
    <p class="holder-name">Tobias Wendlerup</p>
    <p class="holder-role">CEO FYROLT BV</p>
  </div>

  <dl class="contact">
    <dt>Phone</dt><dd>+31 20 517 8036</dd>
    <dt>Direct</dt><dd>+31 20 604 1758</dd>
    <dt>Skype</dt><dd>tobias.fyrolt</dd>
    <dt>Email</dt><dd>ceo@fyrolt.com</dd>
  </dl>

  <address class="address">
    Lindenwerf 38<br>
    1027 HX Amsterdam<br>
    The Netherlands<br>
    <span class="web">www.fyrolt.com</span>
  </address>
</section>

</body>
</html>
```